GLA

Please send us some options for letterhead I attached our Logo. In addition to the Logo we need this information somewhere on the page

48 Harlow Lane
Milbrook, NH 06417
555-274-9160

```html
<!DOCTYPE html>
<html lang="en">
<head>
<meta charset="utf-8">
<title>GLA Letterhead</title>
<link rel="stylesheet" href="https://fonts.googleapis.com/css2?family=Open+Sans:wght@400;700&display=swap">
<style>
  :root {
    --backdrop: #ffffff;
    --paper: #ffffff;
    --brand-dark: #4a3f3b;
    --brand-blue: #1a74b8;
    --text-grey: #444444;
    --glow: #f4f4f4;
  }
  html, body {
    margin: 0;
    padding: 0;
    width: 1200px;
    height: 1200px;
    overflow: hidden;
    background: var(--backdrop);
    font-family: "Open Sans", sans-serif;
  }
  .letterhead {
    position: absolute;
    left: 168px;
    top: 26px;
    width: 864px;
    height: 1150px;
    background: var(--paper);
    overflow: hidden;
  }
  .brand {
    position: absolute;
    top: 50px;
    left: 0;
    right: 0;
    display: flex;
    justify-content: center;
    align-items: center;
    gap: 16px;
  }
  .brand-square {
    width: 72px;
    height: 72px;
    background: var(--brand-dark);
  }
  .brand-name {
    font-size: 64px;
    font-weight: 700;
    color: var(--brand-dark);
    letter-spacing: 2px;
    line-height: 1;
  }
  .brand-glow {
    position: absolute;
    left: 40px;
    bottom: 0;
    width: 784px;
    height: 580px;
    background: radial-gradient(ellipse at 50% 100%, var(--glow) 0%, rgba(255,255,255,0) 70%);
  }
  .contact {
    position: absolute;
    left: 47px;
    bottom: 50px;
    font-size: 13px;
    line-height: 19px;
    color: var(--text-grey);
  }
  .contact-block + .contact-block { margin-top: 20px; }
  .contact-label {
    color: var(--brand-blue);
    font-weight: 700;
  }
</style>
</head>
<body>
  <main class="letterhead">
    <div class="brand-glow" role="img" aria-label="Faint brand decoration rising from the bottom of the page"></div>
    <header class="brand">
      <span class="brand-square"></span>
      <span class="brand-name">GLA</span>
    </header>
    <footer class="contact">
      <div class="contact-block">
        <div class="contact-label">Address:</div>
        <div>48 Harlow Lane, Milbrook, NH&nbsp; 06417</div>
      </div>
      <div class="contact-block">
        <div class="contact-label">Phone:</div>
        <div>555-274-9160</div>
      </div>
    </footer>
  </main>
</body>
</html>
```